Plastic Seasoning Bottle Design Label

I am looking to get a label design that's going on plastic seasoning bottles. My company which deals with seasons/spices. My company sells healthy all natural seasons so I would like the label to have a design of natural. I also would like a hot pepper on there showing it's hot and also other red indentations like red fire or something that shows it's very hot !!!
The company name is Brisk Harvest Table which I would like in light green letters.
There are six different seasonings favors which are:
Barbecue
Garlic
Lemon
Chili
Poultry/Meat
Seafood

The label size: 190.00mm x 111.00mm

Thanks

I would like for the colors to be:
Green
Light Green
Red ( For Hot )
White
Seafood
All of them will be hot as it will show on the label.

Hello, Please include on the labels pictures of the foods associated with the seasoning. Example: Seafood= Fish,lobster,clams,shrimp,scallops,eel,octopus,squid and muscles which will show that it's also very hot. As for seasonings like the Lemon you could just put pictures of lemons which are showing also that there hot as all of the seasoning are hot also. Garlic would be the same as the lemon with just picture also showing it's very hot. Meat would show different kinds of beef such as steak,hamburgers. Also chicken and ham which will show that it's also very hot. Barbecue and Chili you can feel free to show different ideas on that as they will also show that they are very hot as all of them are. The label size is 190.00mm x 111.00mm If you need more time to work on this project please feel free to let me know as I have no problem extending the dead line. Thanks

Hello, In the last update I mentioned Ham as I met to put Ribs not Ham. Thanks

Hello, The budget has been increased. It's now 201.00

Hello, At the end of the company name I would like to have a small TM at the end of the company name as the the has a trade mark on it. Thanks

Industry/Entity Type

Plastic

Font styles to use
Serif
Sans Serif
Decorative
Script
Other font styles liked:
• Georgia,Italic,Bold

```html
<!DOCTYPE html>
<html lang="en">
<head>
<meta charset="utf-8">
<title>Brisk Harvest Table – Seasoning Labels</title>
<link rel="stylesheet" href="https://fonts.googleapis.com/css2?family=Pacifico&family=Nunito:wght@600&display=swap">
<style>
  :root {
    --green: #6cc070;
    --green-text: #62bb5f;
    --white: #ffffff;
    --page: #ffffff;
    --lemon-a: #f5e23a; --lemon-b: #c9e08a;
    --meat-a: #1fa24f; --meat-b: #9fd48a;
    --chili-a: #e8262a; --chili-b: #f0603a;
    --garlic-a: #cfd8d4; --garlic-b: #f7f8f6;
    --bbq-a: #c4202a; --bbq-b: #f0843a;
    --sea-a: #3fb2e6; --sea-b: #d6eef8;
    --flame-core: rgba(255, 190, 60, 0.95);
    --flame-mid: rgba(245, 95, 30, 0.85);
    --flame-edge: rgba(230, 60, 30, 0);
    --food-glow: rgba(255, 255, 255, 0.6);
    --food-edge: rgba(255, 255, 255, 0);
  }
  * { box-sizing: border-box; margin: 0; padding: 0; }
  html, body {
    width: 1200px; height: 2528px; overflow: hidden;
    background: var(--page);
  }
  .sheet {
    display: flex; flex-direction: column; align-items: center;
    gap: 76px; padding-top: 86px;
  }
  .label {
    position: relative; width: 1040px; height: 336px;
    background: var(--white);
    border-top: 6px solid var(--green);
    border-bottom: 6px solid var(--green);
    box-shadow: 0 4px 10px rgba(0,0,0,0.12);
    overflow: hidden;
  }
  .label__art {
    position: absolute; left: 0; top: 0; width: 100%; height: 254px;
  }
  .label--lemon .label__art  { background: linear-gradient(90deg, var(--lemon-a), var(--lemon-b)); }
  .label--meat .label__art   { background: linear-gradient(90deg, var(--meat-a), var(--meat-b)); }
  .label--chili .label__art  { background: linear-gradient(90deg, var(--chili-a), var(--chili-b)); }
  .label--garlic .label__art { background: linear-gradient(90deg, var(--garlic-a), var(--garlic-b)); }
  .label--bbq .label__art    { background: linear-gradient(90deg, var(--bbq-a), var(--bbq-b)); }
  .label--sea .label__art    { background: linear-gradient(90deg, var(--sea-a), var(--sea-b)); }

  .label__flames {
    position: absolute; left: 0; right: 0; top: 110px; height: 144px;
    background: linear-gradient(to top, var(--flame-core) 0%, var(--flame-mid) 40%, var(--flame-edge) 100%);
  }
  .label__food {
    position: absolute; right: 40px; top: 20px; width: 520px; height: 230px;
    border-radius: 50%;
    background: radial-gradient(ellipse at center, var(--food-glow) 0%, var(--food-edge) 70%);
  }

  .label__flavor {
    position: absolute; left: 56px; top: 74px;
    font-family: "Pacifico", cursive; font-weight: 400;
    font-size: 124px; line-height: 1.3;
    color: var(--white);
    transform: rotate(-6deg); transform-origin: left bottom;
    white-space: nowrap;
  }
  .label--bbq .label__flavor { font-size: 108px; top: 88px; }
  .label--sea .label__flavor { font-size: 112px; top: 84px; }

  .label__company {
    position: absolute; left: 46px; top: 258px;
    font-family: "Nunito", sans-serif; font-weight: 600;
    font-size: 32px; line-height: 70px;
    color: var(--green-text);
  }
  .label__tm { font-size: 14px; vertical-align: super; line-height: 0; margin-left: 2px; }
  .label__mark {
    position: absolute; right: 34px; top: 262px;
    display: flex; align-items: center; gap: 10px;
    font-family: "Nunito", sans-serif; font-weight: 600;
    font-size: 28px; line-height: 60px;
    color: var(--green-text);
  }
  .label__mark::before {
    content: ""; width: 22px; height: 22px; border-radius: 50%;
    background: var(--green);
  }
</style>
</head>
<body>
<main class="sheet">
  <section class="label label--lemon">
    <div class="label__art"></div>
    <div class="label__flames" role="img" aria-label="Row of hot flames"></div>
    <div class="label__food" role="img" aria-label="Sketched lemons in flames"></div>
    <h2 class="label__flavor">Lemon</h2>
    <p class="label__company">Brisk Harvest Table<span class="label__tm">TM</span></p>
    <p class="label__mark">Greenleaf Grade</p>
  </section>
  <section class="label label--meat">
    <div class="label__art"></div>
    <div class="label__flames" role="img" aria-label="Row of hot flames"></div>
    <div class="label__food" role="img" aria-label="Sketched roast chicken, steak and ribs in flames"></div>
    <h2 class="label__flavor">Meat</h2>
    <p class="label__company">Brisk Harvest Table<span class="label__tm">TM</span></p>
    <p class="label__mark">Greenleaf Grade</p>
  </section>
  <section class="label label--chili">
    <div class="label__art"></div>
    <div class="label__flames" role="img" aria-label="Row of hot flames"></div>
    <div class="label__food" role="img" aria-label="Sketched hot chili pepper in flames"></div>
    <h2 class="label__flavor">Chili</h2>
    <p class="label__company">Brisk Harvest Table<span class="label__tm">TM</span></p>
    <p class="label__mark">Greenleaf Grade</p>
  </section>
  <section class="label label--garlic">
    <div class="label__art"></div>
    <div class="label__flames" role="img" aria-label="Row of hot flames"></div>
    <div class="label__food" role="img" aria-label="Sketched garlic bulbs in flames"></div>
    <h2 class="label__flavor">Garlic</h2>
    <p class="label__company">Brisk Harvest Table<span class="label__tm">TM</span></p>
    <p class="label__mark">Greenleaf Grade</p>
  </section>
  <section class="label label--bbq">
    <div class="label__art"></div>
    <div class="label__flames" role="img" aria-label="Row of hot flames"></div>
    <div class="label__food" role="img" aria-label="Sketched barbecue grill and tools in flames"></div>
    <h2 class="label__flavor">Barbecue</h2>
    <p class="label__company">Brisk Harvest Table<span class="label__tm">TM</span></p>
    <p class="label__mark">Greenleaf Grade</p>
  </section>
  <section class="label label--sea">
    <div class="label__art"></div>
    <div class="label__flames" role="img" aria-label="Row of hot flames"></div>
    <div class="label__food" role="img" aria-label="Sketched lobster and shrimp in flames"></div>
    <h2 class="label__flavor">Seafood</h2>
    <p class="label__company">Brisk Harvest Table<span class="label__tm">TM</span></p>
    <p class="label__mark">Greenleaf Grade</p>
  </section>
</main>
</body>
</html>
```